Business Card Design

My company is a health food catering and delivery business. Our colours are a bright turquiose green/blue, black, white and natural brown based beige. I would like the front of my card (working from the outside in; with a turquoise green boarder -quite thick, with a thin black line separating the turquoise boarder from the beige inside the remaining space of the front of the card with my logo in the centre. This should be all that appears on the front.

On the back I would like all the information displayed above on the beige coloured card, with the blurb in the bright turquoise and my contact information in black please. I would like my business name central - Harvest Lantern Kitchen and immediately below with a right alignment - ...Dine with Delight
Below this should follow all that I have displayed above with a left alignment.

Target Market(s)

Cafes, restaurants, individuals, buying agents & super markets

Industry/Entity Type

Catering

Contact Information for Business Card

BACK OF BUSINESS CARD:
Harvest Lantern Kitchen
...Dine with Delight
Deliciously healthy foods - free from gluten, lactose, cane sugar, trans-fat, GMO corn, soy & rice, no artificial flavours, colours or preservatives.
Prepared fresh from locally sourced ingredients, delivered to your door! For individuals, families, corporate, cafes, restaurants & event catering for Toowoomba & surrounds!

PH: 0491 382 907 // orders@harvestlanternkitchen.example
www.harvestlanternkitchen.example
www.social.example/harvestlanternkitchen

Requirements
Must have
• Please supply a modern, easy to read text that will blend nicely with my logo text.
Nice to have
• I really want my business cards to stand out as these will be the template for brochures, menus and website designers to draw inspiration from!
Should not have
• Please do not use Arial, Tahoma or Times Roman text.

```html
<!DOCTYPE html>
<html lang="en">
<head>
<meta charset="utf-8">
<title>Harvest Lantern Kitchen – Business Card</title>
<link rel="stylesheet" href="https://fonts.googleapis.com/css2?family=Mulish:wght@700&family=Didact+Gothic&display=swap">
<style>
  :root {
    --turquoise: #22bec3;
    --beige: #f6dec6;
    --ink: #2c3a3a;
    --body-ink: #3b3b3b;
    --rule-light: #4e8a84;
    --rule-dark: #1d2b29;
    --glow: #e4dcc5;
    --glow-edge: #6cc3c4;
  }
  html, body {
    margin: 0;
    padding: 0;
    width: 972px;
    height: 1200px;
    overflow: hidden;
    background: #ffffff;
  }
  .canvas {
    position: relative;
    width: 972px;
    height: 1200px;
  }
  .card {
    position: absolute;
    left: 57px;
    width: 858px;
    overflow: hidden;
  }

  /* Info side */
  .card--info {
    top: 67px;
    height: 465px;
    background: var(--beige);
    border-top: 30px solid var(--turquoise);
    border-bottom: 30px solid var(--turquoise);
    box-sizing: border-box;
  }
  .brand-title {
    position: absolute;
    left: 0;
    width: 100%;
    top: 22px;
    margin: 0;
    font-family: "Mulish", "Century Gothic", sans-serif;
    font-weight: 700;
    font-size: 39px;
    line-height: 44px;
    color: var(--ink);
    text-align: center;
    text-indent: -36px;
  }
  .tagline {
    position: absolute;
    right: 218px;
    top: 74px;
    margin: 0;
    font-family: "Mulish", "Century Gothic", sans-serif;
    font-weight: 700;
    font-size: 39px;
    line-height: 44px;
    color: var(--ink);
  }
  .blurb {
    position: absolute;
    left: 24px;
    top: 130px;
    margin: 0;
    font-family: "Didact Gothic", "Century Gothic", sans-serif;
    font-size: 17.2px;
    line-height: 22px;
    color: var(--body-ink);
    white-space: nowrap;
  }
  .blurb span { display: block; }
  .contacts {
    position: absolute;
    left: 112px;
    top: 252px;
    margin: 0;
    padding: 0;
    list-style: none;
    font-family: "Didact Gothic", "Century Gothic", sans-serif;
    font-size: 27px;
    color: var(--ink);
  }
  .contacts li {
    display: flex;
    align-items: center;
    height: 34px;
  }
  .contact-icon {
    width: 26px;
    height: 26px;
    margin-right: 24px;
    flex: none;
  }

  /* Logo side */
  .card--logo {
    top: 666px;
    height: 466px;
    background: var(--turquoise);
  }
  .logo-field {
    position: absolute;
    left: 0;
    top: 97px;
    width: 100%;
    height: 326px;
    border-top: 13px solid var(--rule-dark);
    border-bottom: 13px solid var(--rule-dark);
    border-image: linear-gradient(90deg, var(--rule-light), var(--rule-dark)) 1;
    box-sizing: border-box;
    background: radial-gradient(ellipse 55% 75% at 50% 55%, var(--glow) 0%, #b8d6cc 55%, var(--glow-edge) 100%);
    display: flex;
    align-items: center;
    justify-content: center;
  }
  .logo-mark {
    display: flex;
    align-items: center;
    gap: 18px;
  }
  .logo-dot {
    width: 30px;
    height: 30px;
    border-radius: 50%;
    background: var(--ink);
  }
  .logo-name {
    font-family: "Mulish", "Century Gothic", sans-serif;
    font-weight: 700;
    font-size: 46px;
    color: var(--ink);
  }
</style>
</head>
<body>
<div class="canvas">

  <section class="card card--info">
    <h1 class="brand-title">Harvest Lantern Kitchen</h1>
    <p class="tagline">............Dine with Delight</p>
    <p class="blurb">
      <span>Deliciously healthy foods - free from gluten, lactose, cane sugar, trans-fat, GMO corn,</span>
      <span>soy &amp; rice, no artificial flavours, colours or preservatives.</span>
      <span>Prepared fresh from locally sourced ingredients, delivered to your door! For individuals,</span>
      <span>families, corporate, cafes, restaurants &amp; event catering for Toowoomba &amp; surrounds!</span>
    </p>
    <ul class="contacts">
      <li>
        <svg class="contact-icon" viewBox="0 0 26 26" aria-hidden="true">
          <circle cx="13" cy="13" r="12.5" fill="#1e9fae"/>
          <path d="M6 11 q7-5 14 0 l-1 2 -3-1 v-1.5 q-3-1 -6 0 v1.5 l-3 1z" fill="#fff"/>
          <rect x="8" y="13.5" width="10" height="5" rx="1.5" fill="#fff"/>
        </svg>
        0491 382 907
      </li>
      <li>
        <svg class="contact-icon" viewBox="0 0 26 26" aria-hidden="true">
          <circle cx="13" cy="13" r="12.5" fill="#1e9fae"/>
          <rect x="6" y="8" width="14" height="10" fill="none" stroke="#fff" stroke-width="1.6"/>
          <path d="M6 8 l7 6 7-6 M6 18 l5-5 M20 18 l-5-5" fill="none" stroke="#fff" stroke-width="1.4"/>
        </svg>
        orders@harvestlanternkitchen.example
      </li>
      <li>
        <svg class="contact-icon" viewBox="0 0 26 26" aria-hidden="true">
          <circle cx="13" cy="13" r="12.5" fill="#1e9fae"/>
        </svg>
        www.social.example/harvestlanternkitchen
      </li>
      <li>
        <svg class="contact-icon" viewBox="0 0 26 26" aria-hidden="true">
          <circle cx="13" cy="13" r="12.5" fill="#1e9fae"/>
          <circle cx="13" cy="13" r="7" fill="none" stroke="#fff" stroke-width="1.6"/>
          <path d="M6 13 h14 M13 6 q-4 7 0 14 M13 6 q4 7 0 14" fill="none" stroke="#fff" stroke-width="1.2"/>
        </svg>
        www.harvestlanternkitchen.example
      </li>
    </ul>
  </section>

  <section class="card card--logo">
    <div class="logo-field" role="img" aria-label="Harvest Lantern Kitchen logo: chef illustration with the business name">
      <div class="logo-mark">
        <span class="logo-dot"></span>
        <span class="logo-name">Harvest Lantern Kitchen</span>
      </div>
    </div>
  </section>

</div>
</body>
</html>
```